Banner dimension 1767 X 887 for Tolvenko website

Need one banner for our website www.tolvenko.com.au, The dimension of the banner should be 1767 x 887. Attached to this brief are two images that needs to be on that one banner, PLEASE DO NOT SEND SEPARATE BANNERS, both images on the same banner. Thanks

The banner should have the following message on it:

1.) " Take a further 40% off all stock" ( use code: TOLVENKO. Ends 31/12/2015)
2.) " Kick back or kick it up a notch this Autumn in the most versatile pique striped polo shirts and Pinafore belt strap denim dress"

Target Market(s)

kids aged 5-12yrs

Requirements
Must have
• very playful

```html
<!DOCTYPE html>
<html lang="en">
<head>
<meta charset="utf-8">
<title>Tolvenko – Further 40% Off Banner</title>
<link rel="stylesheet" href="https://fonts.googleapis.com/css2?family=Open+Sans:wght@700;800&family=Alegreya+Sans+SC:wght@800&display=swap">
<style>
  :root {
    --page-bg: #1c1c1c;
    --sky-top: #8fcbef;
    --sky-mid: #d3ecfb;
    --sky-bottom: #c3e6fa;
    --floor: #34261a;
    --floor-dark: #1f1610;
    --promo-blue: #0aa3e8;
    --promo-green: #8cc43f;
    --ink: #111111;
    --white: #ffffff;
    --denim: #5a7fa3;
    --skin: #d9a98e;
    --polo-green: #4f8a63;
  }
  * { margin: 0; padding: 0; box-sizing: border-box; }
  html, body {
    width: 1200px;
    height: 900px;
    overflow: hidden;
    background: var(--page-bg);
  }
  .banner {
    position: absolute;
    left: 16px;
    top: 130px;
    width: 1169px;
    height: 587px;
    overflow: hidden;
  }
  .sky {
    position: absolute;
    inset: 0;
    background:
      radial-gradient(ellipse 460px 300px at 590px 0px, rgba(255,255,255,0.97), rgba(255,255,255,0) 100%),
      radial-gradient(ellipse 260px 160px at 120px 60px, rgba(255,255,255,0.55), rgba(255,255,255,0) 100%),
      radial-gradient(ellipse 300px 180px at 1050px 80px, rgba(255,255,255,0.5), rgba(255,255,255,0) 100%),
      linear-gradient(180deg, var(--sky-top) 0%, var(--sky-mid) 50%, var(--sky-bottom) 100%);
  }
  .floor {
    position: absolute;
    left: 0;
    top: 510px;
    width: 100%;
    height: 77px;
    background: linear-gradient(180deg, var(--floor) 0%, var(--floor-dark) 100%);
  }
  .kid-photo {
    position: absolute;
    border-radius: 90px 90px 24px 24px;
  }
  .kid-photo--girl {
    left: 106px;
    top: 118px;
    width: 222px;
    height: 440px;
    background: linear-gradient(180deg, rgba(217,169,142,0.75) 0%, rgba(240,240,240,0.8) 20%, rgba(90,127,163,0.85) 35%, rgba(90,127,163,0.8) 65%, rgba(217,169,142,0.7) 80%, rgba(230,90,140,0.8) 100%);
  }
  .kid-photo--boy {
    left: 262px;
    top: 168px;
    width: 256px;
    height: 390px;
    background: linear-gradient(180deg, rgba(217,169,142,0.75) 0%, rgba(79,138,99,0.85) 25%, rgba(79,138,99,0.8) 48%, rgba(120,150,180,0.8) 60%, rgba(217,169,142,0.7) 82%, rgba(40,40,40,0.8) 100%);
  }
  .promo {
    position: absolute;
    inset: 0;
    width: 1169px;
    height: 587px;
  }
  .promo-code {
    font-family: "Open Sans", Arial, sans-serif;
    font-weight: 700;
    font-size: 26px;
    fill: var(--ink);
  }
  .promo-ends {
    font-family: "Open Sans", Arial, sans-serif;
    font-weight: 700;
    font-size: 24px;
    fill: var(--white);
  }
  .promo-headline {
    font-family: "Open Sans", Arial, sans-serif;
    font-weight: 800;
    font-size: 31px;
    fill: var(--white);
  }
  .promo-headline .percent { font-size: 39px; }
  .tagline {
    position: absolute;
    left: 557px;
    top: 340px;
    font-family: "Alegreya Sans SC", Arial, sans-serif;
    font-weight: 800;
    font-size: 32px;
    line-height: 37.5px;
    letter-spacing: 1.6px;
    color: var(--ink);
  }
  .tagline-line {
    display: block;
    white-space: nowrap;
  }
</style>
</head>
<body>
  <div class="banner">
    <div class="sky" role="img" aria-label="Bright blue autumn sky with sun rays, soft clouds and bokeh light circles"></div>
    <div class="floor" role="img" aria-label="Dark wooden floorboards"></div>
    <div class="kid-photo kid-photo--girl" role="img" aria-label="Smiling girl with long hair in a white tee, denim pinafore dress and pink sneakers"></div>
    <div class="kid-photo kid-photo--boy" role="img" aria-label="Playful boy leaning and waving in a green striped polo shirt, denim shorts and sneakers"></div>

    <svg class="promo" viewBox="0 0 1169 587">
      <polygon points="866,143 1169,127 1169,168 866,182" fill="var(--promo-green)"/>
      <polygon points="422,202 1169,166 1169,232 422,270" fill="var(--promo-blue)"/>
      <text class="promo-code" x="571" y="191" transform="rotate(-3 571 191)">use code: TOLVENKO</text>
      <text class="promo-ends" x="925" y="165" transform="rotate(-3 925 165)">Ends 31/12/2015</text>
      <text class="promo-headline" x="517" y="247" transform="rotate(-3 517 247)">TAKE A FURTHER <tspan class="percent">40%</tspan> OFF ALL STOCK</text>
    </svg>

    <p class="tagline">
      <span class="tagline-line">Kick back or kick it up a notch this</span>
      <span class="tagline-line">Autumn in the most versatile pique</span>
      <span class="tagline-line">striped polo shirts and Pinafore</span>
      <span class="tagline-line">belt strap denim dress</span>
    </p>
  </div>
</body>
</html>
```